Salon and Spa Distributor Business Card

Need a business card. We are are distributor in the salon and spa industry. We identify with natural beauty. Need a card with:
Company Name: Petal Harbor"
Title: "President & CEO"
Address
Company Phone number
email
website
Tag Line:" The Professional Salon Source"

Industry/Entity Type

Business

Contact Information for Business Card

Name: Leo Mendoza
Title: "President & CEO"
Address: 317 Birchline Ave, Westbrook, NJ 08412
Company Phone number: 800-463-5108
email: leomendoza@petalharbor-example.com
website: www.petalharbor-example.com

Requirements
Should not have
• No black backgrounds

```html
<!DOCTYPE html>
<html lang="en">
<head>
<meta charset="utf-8">
<title>Petal Harbor – Business Card</title>
<link rel="stylesheet" href="https://fonts.googleapis.com/css2?family=Questrial&family=Mulish:ital,wght@1,300&family=Outfit:wght@400;600&display=swap">
<style>
  :root {
    --page: #ffffff;
    --ink: #111111;
    --brand-green: #4a9a4a;
    --brand-light: #62b846;
    --brand-dark: #006837;
    --card-white: #ffffff;
    --card-line: #222222;
  }
  html, body {
    margin: 0;
    padding: 0;
    width: 1200px;
    height: 1200px;
    overflow: hidden;
    background: var(--page);
  }
  .sheet {
    position: relative;
    width: 1200px;
    height: 1200px;
  }
  .card {
    position: absolute;
    top: 422px;
    width: 549px;
    height: 314px;
    box-sizing: border-box;
  }
  .card--front {
    left: 27px;
    background: var(--card-white);
    border: 1px solid var(--card-line);
  }
  .card--back {
    left: 625px;
    background: linear-gradient(90deg, var(--brand-dark) 0%, #3a963f 45%, var(--brand-light) 100%);
  }
  .brand-mark {
    position: absolute;
    left: 48px;
    top: 92px;
    width: 130px;
    height: 130px;
    border-radius: 50%;
    background: var(--brand-light);
  }
  .brand-name {
    position: absolute;
    left: 222px;
    top: 130px;
    margin: 0;
    font-family: "Questrial", sans-serif;
    font-weight: 400;
    font-size: 50px;
    line-height: 1;
    color: var(--brand-green);
    letter-spacing: -0.5px;
  }
  .tagline {
    position: absolute;
    left: 238px;
    top: 198px;
    margin: 0;
    font-family: "Mulish", sans-serif;
    font-style: italic;
    font-weight: 300;
    font-size: 19px;
    line-height: 1;
    color: var(--brand-green);
    letter-spacing: 0.3px;
  }
  .contact {
    position: absolute;
    left: 279px;
    top: 76px;
    margin: 0;
    padding: 0;
    list-style: none;
    font-family: "Outfit", sans-serif;
    color: var(--card-white);
  }
  .contact__title {
    font-weight: 600;
    font-size: 19px;
    margin-bottom: 14px;
  }
  .contact__line {
    font-weight: 400;
    font-size: 14px;
    line-height: 1;
    margin-bottom: 15px;
  }
  .side-label {
    position: absolute;
    top: 764px;
    width: 200px;
    margin: 0;
    text-align: center;
    font-family: "Outfit", sans-serif;
    font-size: 24px;
    font-weight: 400;
    color: var(--ink);
  }
  .side-label--front { left: 180px; }
  .side-label--back { left: 799px; }
</style>
</head>
<body>
<main class="sheet">
  <section class="card card--front" aria-label="Card front">
    <span class="brand-mark" aria-hidden="true"></span>
    <h1 class="brand-name">PetalHarbor</h1>
    <p class="tagline">The Professional Salon Source</p>
  </section>
  <p class="side-label side-label--front">Front</p>

  <section class="card card--back" aria-label="Card back">
    <ul class="contact">
      <li class="contact__title">President &amp; CEO</li>
      <li class="contact__line">317 Birchline Ave, Westbrook, NJ 08412</li>
      <li class="contact__line">800-463-5108</li>
      <li class="contact__line">leomendoza@petalharbor-example.com</li>
      <li class="contact__line">www.petalharbor-example.com</li>
    </ul>
  </section>
  <p class="side-label side-label--back">Back</p>
</main>
</body>
</html>
```